DRIFTFRAME studio

Design to be modern with colours of logo, maybe orange background. Include name, position, phone/WhatsApp email/web. Specialises in long form TIMELAPSE

Contact Information for Business Card

Marcus Ellery, filmmaker,/photographer, phone/WhatsApp +971528306457, email - marcus@driftframestudio.example www.driftframestudio.example, instagram @driftframestudio

Font styles to use
Sans Serif

Requirements
Must have
• Fresh, bright, modern, original
Marcus Ellery - Filmmaker/Photographer
Phone/WhatsApp +971 528 30 6457
email - marcus@driftfarmestudio.example
Web - driftfarmestudio.example
PoBox 584193, Dubai, UAE
instagram - driftframestudio
Should not have
• solid black background

```html
<!DOCTYPE html>
<html lang="en">
<head>
<meta charset="utf-8">
<title>DRIFTFRAME studio – Business Card</title>
<link href="https://fonts.googleapis.com/css2?family=Montserrat:wght@800&family=Quicksand:wght@500;600&display=swap" rel="stylesheet">
<style>
  :root {
    --orange: #f47421;
    --ink: #111111;
    --paper: #ffffff;
    --stage: #2c2c2c;
  }
  * { margin: 0; padding: 0; box-sizing: border-box; }
  html, body { width: 1200px; height: 900px; overflow: hidden; background: var(--stage); }
  .stage {
    width: 1200px; height: 900px;
    display: flex; flex-direction: column; align-items: center; justify-content: center; gap: 24px;
  }
  .card {
    position: relative; width: 760px; height: 410px; overflow: hidden;
    font-family: "Quicksand", sans-serif;
  }
  .card--front { background: var(--orange); color: var(--paper); }
  .front-brand {
    position: absolute; left: 0; right: 0; top: 150px; text-align: center;
    font-family: "Montserrat", sans-serif; font-weight: 800; font-size: 58px;
    letter-spacing: 1px; color: var(--paper);
  }
  .front-web {
    position: absolute; left: 0; right: 0; bottom: 34px; text-align: center;
    font-size: 21px; font-weight: 600; letter-spacing: 0.5px;
  }
  .card--back { background: var(--paper); }
  .back-wave { position: absolute; inset: 0; }
  .back-brand {
    position: absolute; left: 40px; top: 58px;
    font-family: "Montserrat", sans-serif; font-weight: 800; font-size: 34px;
    color: var(--orange); display: flex; align-items: center; gap: 12px;
  }
  .back-brand .dot { width: 22px; height: 22px; border-radius: 50%; background: var(--orange); }
  .holder { position: absolute; right: 40px; top: 130px; text-align: right; }
  .holder-name {
    font-family: "Montserrat", sans-serif; font-weight: 800; font-size: 24px;
    letter-spacing: 5px; color: var(--orange);
  }
  .holder-role { font-size: 18px; font-weight: 600; color: var(--ink); margin-top: 2px; }
  .contact {
    position: absolute; right: 40px; top: 270px; text-align: right;
    color: var(--ink); font-size: 18px; font-weight: 600; line-height: 1.3;
  }
  .contact-address { margin-bottom: 10px; }
  .contact-line { display: flex; align-items: center; justify-content: flex-end; gap: 12px; }
  .contact-icon { width: 18px; height: 18px; flex: none; }
</style>
</head>
<body>
<main class="stage">
  <section class="card card--front">
    <div class="front-brand">DRIFTFRAME studio</div>
    <div class="front-web">www.driftframestudio.example</div>
  </section>

  <section class="card card--back">
    <svg class="back-wave" viewBox="0 0 760 410" aria-hidden="true">
      <path d="M0 290 C 220 270, 420 150, 760 210 L760 230 C 440 170, 240 300, 0 318 Z" fill="var(--ink)"/>
      <path d="M0 318 C 240 300, 440 170, 760 230 L760 410 L0 410 Z" fill="var(--orange)"/>
    </svg>

    <div class="back-brand"><span class="dot"></span>DRIFTFRAME studio</div>

    <div class="holder">
      <div class="holder-name">MARCUS ELLERY</div>
      <div class="holder-role">Flmmaker/photographer</div>
    </div>

    <div class="contact">
      <div class="contact-address">PoBox 584193, Dubai, UAE</div>
      <div class="contact-line">+971 528 30 6457
        <svg class="contact-icon" viewBox="0 0 18 18"><circle cx="9" cy="9" r="7.5" fill="none" stroke="var(--ink)" stroke-width="1.6"/></svg>
      </div>
      <div class="contact-line">@driftframestudio
        <svg class="contact-icon" viewBox="0 0 18 18"><circle cx="9" cy="9" r="7.5" fill="none" stroke="var(--ink)" stroke-width="1.6"/></svg>
      </div>
      <div class="contact-line">marcus@driftframestudio.example
        <svg class="contact-icon" viewBox="0 0 18 18"><rect x="1.5" y="4" width="15" height="10" fill="none" stroke="var(--ink)" stroke-width="1.6"/><path d="M1.5 4 L9 10 L16.5 4" fill="none" stroke="var(--ink)" stroke-width="1.6"/></svg>
      </div>
      <div class="contact-line">www.driftframestudio.example
        <svg class="contact-icon" viewBox="0 0 18 18"><circle cx="9" cy="9" r="7.5" fill="none" stroke="var(--ink)" stroke-width="1.6"/><ellipse cx="9" cy="9" rx="3.2" ry="7.5" fill="none" stroke="var(--ink)" stroke-width="1.4"/><path d="M1.5 9 H16.5" stroke="var(--ink)" stroke-width="1.4"/></svg>
      </div>
    </div>
  </section>
</main>
</body>
</html>
```